Corvane Property Group Business cards

I am starting a property development and consultancy business called Corvane Property Group. I have a logo designed and a website on its way:
www.corvanegroup-example.com.au

I need a business card with the following:

Front:
Mostly orange with logo taking up all front of card

Back of card:
Logo

Mark Dellaway
Managing Director

T +61 452 907 364
E mark.dellaway@corvanegroup-example.com.au
www.corvanegroup-example.com.au

Industry/Entity Type

Business

Requirements
Must have
• curved edges

```html
<!DOCTYPE html>
<html lang="en">
<head>
<meta charset="utf-8">
<title>Corvane Property Group – Business Cards</title>
<link rel="stylesheet" href="https://fonts.googleapis.com/css2?family=Arimo:wght@400;700&display=swap">
<style>
  :root {
    --stage: #000000;
    --card: #ffffff;
    --orange: #f7a631;
    --ink: #2e2e2e;
    --rule: #555555;
  }
  * { box-sizing: border-box; margin: 0; padding: 0; }
  html, body {
    width: 1200px;
    height: 420px;
    overflow: hidden;
    background: var(--stage);
    font-family: "Arimo", Arial, sans-serif;
  }
  .canvas {
    position: relative;
    width: 1200px;
    height: 420px;
  }
  .card {
    position: absolute;
    top: 65px;
    width: 537px;
    height: 297px;
    background: var(--card);
    border-radius: 24px;
    overflow: hidden;
  }
  .card--front { left: 40px; }
  .card--back { left: 620px; }

  /* Front */
  .front-panel {
    position: absolute;
    left: 42px;
    top: 43px;
    width: 450px;
    height: 164px;
    background: var(--orange);
    display: flex;
    align-items: center;
    justify-content: center;
  }
  .front-name {
    color: var(--card);
    font-weight: 400;
    font-size: 35px;
    letter-spacing: 0.5px;
    white-space: nowrap;
  }

  /* Back */
  .back-band {
    position: absolute;
    left: 0;
    top: 0;
    width: 100%;
    height: 92px;
    background: var(--orange);
    display: flex;
    align-items: center;
    justify-content: center;
  }
  .back-name {
    color: var(--card);
    font-weight: 400;
    font-size: 27px;
    letter-spacing: 0.5px;
    white-space: nowrap;
  }
  .contact {
    position: absolute;
    left: 63px;
    top: 128px;
    width: 420px;
  }
  .person-name {
    color: var(--orange);
    font-weight: 700;
    font-size: 24px;
    line-height: 30px;
  }
  .person-role {
    color: var(--ink);
    font-size: 17px;
    line-height: 22px;
  }
  .divider {
    display: block;
    width: 414px;
    height: 3px;
    margin: 10px 0 8px;
  }
  .contact-line {
    color: var(--ink);
    font-size: 16.5px;
    line-height: 21.5px;
    white-space: nowrap;
  }
  .contact-label {
    color: var(--orange);
    font-weight: 700;
  }
  .contact-web {
    color: var(--orange);
    font-weight: 700;
  }
</style>
</head>
<body>
<main class="canvas">
  <section class="card card--front" aria-label="Card front">
    <div class="front-panel">
      <span class="front-name">Corvane Property Group</span>
    </div>
  </section>

  <section class="card card--back" aria-label="Card back">
    <div class="back-band">
      <span class="back-name">Corvane Property Group</span>
    </div>
    <div class="contact">
      <p class="person-name">Mark Dellaway</p>
      <p class="person-role">Managing Director</p>
      <svg class="divider" viewBox="0 0 414 3" aria-hidden="true">
        <line x1="1" y1="1.5" x2="414" y2="1.5" stroke="var(--rule)" stroke-width="1.5" stroke-dasharray="1.5 3.5" stroke-linecap="round"/>
      </svg>
      <p class="contact-line"><span class="contact-label">Tel.:</span> +61 452 907 364</p>
      <p class="contact-line"><span class="contact-label">E-mail:</span> mark.dellaway@corvanegroup-example.com.au</p>
      <p class="contact-line contact-web">www.corvanegroup-example.com.au</p>
    </div>
  </section>
</main>
</body>
</html>
```